Business Card Design Project for - The Brackenfold Lawncare Company Ltd. We are a Landscape and garden

I would like designer to use all special glosses etc so i can have a professional looking business card. The theme of the business card can reflect that of the Logo attached by ArtVellum or your own unique ideas.. please feel free to go wild as i hope i can select a winner i like - my budget will be committed so please get involved. Good luck and thank you Neville

Target Market(s)

Must look Professional

General Public and Businesses including Councils, Local Government, Hospitals, Hotels, Professionals and Professional Sports People.

Industry/Entity Type

Landscape Gardening

Contact Information for Business Card

The Brackenfold Lawncare Company Ltd

Mr R.P Ashworth
Head Office - Quayline Park Manchester
t. 0772 458 916
e. info@brackenfoldlawn.co.uk
w. www.brackenfoldlawn.co.uk

Facebook - https://www.pagemural.com/TheBrackenfoldLawncareCompany/
Twitter - https://chirpline.com/ThePlotTruck
Instagram - https://www.snapquilt.com/thebrackenfoldlawncarecompany/?hl=en
Google+ - https://circles.vondarix.com/u/0/208475932610482739516
Yelp - https://www.localrava.co.uk/biz/the-brackenfold-lawncare-company-manchester-4

Font styles to use
Serif
Script
Other font styles liked:
• I don't have much of an idea of font types sorry

Colors

Designer to choose colors to be used in the design.

Requirements
Must have
• A Professional look and Design
• Special effects with gloss and fading of colours possibly..
• Front and back design
Nice to have
• All special features with effects and gloss etc

```html
<!DOCTYPE html>
<html lang="en">
<head>
<meta charset="utf-8">
<title>The Brackenfold Lawncare Company Ltd – Business Card</title>
<link rel="stylesheet" href="https://fonts.googleapis.com/css2?family=Cinzel:wght@400;600&display=swap">
<style>
  :root {
    --backdrop: #3a3a3a;
    --card-top: #2b2b2b;
    --card-bottom: #111111;
    --text-silver: #b9b9b9;
    --text-dim: #9a9a9a;
    --accent-green: #3fb64a;
    --accent-green-dark: #1f8a2e;
    --icon-disc: #a9a9a9;
    --icon-ink: #2a2a2a;
  }
  * { margin: 0; padding: 0; box-sizing: border-box; }
  html, body {
    width: 1200px; height: 900px; overflow: hidden;
    background: var(--backdrop);
    font-family: "Cinzel", "Times New Roman", serif;
  }
  .stage {
    position: relative; width: 1200px; height: 900px;
    display: flex; justify-content: center; align-items: center; gap: 80px;
  }
  .card {
    position: relative; width: 380px; height: 680px;
    border-radius: 28px;
    background: linear-gradient(160deg, var(--card-top) 0%, #1b1b1b 55%, var(--card-bottom) 100%);
    box-shadow: 0 18px 40px rgba(0,0,0,.55), inset 0 1px 0 rgba(255,255,255,.08);
    color: var(--text-silver);
    text-align: center;
    overflow: hidden;
  }
  .card::after {
    content: ""; position: absolute; inset: 0; border-radius: 28px; pointer-events: none;
    background: linear-gradient(125deg, rgba(255,255,255,.07) 0%, rgba(255,255,255,0) 45%);
  }

  /* Front */
  .holder { position: absolute; top: 92px; left: 0; right: 0; }
  .holder-name { font-size: 27px; font-weight: 400; letter-spacing: 1px; }
  .holder-role { font-size: 17px; color: var(--text-dim); margin-top: 2px; }

  .brand { position: absolute; left: 0; right: 0; }
  .front .brand { top: 218px; }
  .back .brand { top: 88px; }
  .brand-mark {
    width: 64px; height: 64px; margin: 0 auto 14px; border-radius: 50%;
    background: var(--accent-green);
  }
  .brand-name, .brand-sub { font-weight: 400; color: var(--text-silver); line-height: 1.15; }
  .brand-name { font-size: 31px; letter-spacing: 1px; }
  .brand-sub { font-size: 11.5px; letter-spacing: 3px; margin-top: 4px; }

  .office { position: absolute; top: 418px; left: 0; right: 0; font-size: 18px; line-height: 1.35; color: var(--text-dim); }

  .contact-icons {
    position: absolute; top: 500px; left: 0; right: 0;
    display: flex; justify-content: center; gap: 28px;
  }
  .contact-icons svg { width: 36px; height: 36px; }

  .contact-lines { position: absolute; top: 562px; left: 0; right: 0; font-size: 15px; line-height: 1.55; letter-spacing: .5px; }
  .contact-lines .phone { font-size: 19px; }
  .highlight { color: var(--accent-green); }

  /* Back */
  .social-list { position: absolute; top: 258px; left: 0; right: 0; list-style: none; }
  .social-item { margin-bottom: 17px; }
  .social-badge {
    display: block; width: 24px; height: 24px; margin: 0 auto 7px; border-radius: 3px;
    background: linear-gradient(180deg, var(--accent-green), var(--accent-green-dark));
  }
  .social-handle { font-size: 13px; color: var(--text-silver); letter-spacing: .3px; }
  .social-handle.long { font-size: 11px; }
</style>
</head>
<body>
<main class="stage">

  <section class="card front" aria-label="Business card front">
    <div class="holder">
      <p class="holder-name">R.P Ashworth</p>
      <p class="holder-role">Managing Director</p>
    </div>

    <div class="brand">
      <div class="brand-mark"></div>
      <p class="brand-name">THE BRACKENFOLD</p>
      <p class="brand-sub">LAWNCARE COMPANY LTD</p>
    </div>

    <p class="office">Head Office<br>Quayline Park Manchester</p>

    <div class="contact-icons">
      <svg viewBox="0 0 36 36" aria-label="Phone">
        <circle cx="18" cy="18" r="18" fill="var(--icon-disc)"/>
        <path d="M10 15 q8 -6 16 0 l-1.5 3 h-3 l-.8 -2 h-5.4 l-.8 2 h-3 z" fill="var(--icon-ink)"/>
        <rect x="12" y="19" width="12" height="7" rx="1.5" fill="var(--icon-ink)"/>
      </svg>
      <svg viewBox="0 0 36 36" aria-label="Email">
        <circle cx="18" cy="18" r="18" fill="var(--icon-disc)"/>
        <rect x="9" y="12" width="18" height="12" fill="var(--icon-ink)"/>
        <polyline points="9,12 18,19 27,12" fill="none" stroke="var(--icon-disc)" stroke-width="1.5"/>
      </svg>
      <svg viewBox="0 0 36 36" aria-label="Website">
        <circle cx="18" cy="18" r="18" fill="var(--icon-disc)"/>
        <g fill="none" stroke="var(--icon-ink)" stroke-width="2.4" transform="rotate(-45 18 18)">
          <rect x="8" y="14.5" width="11" height="7" rx="3.5"/>
          <rect x="17" y="14.5" width="11" height="7" rx="3.5"/>
        </g>
      </svg>
    </div>

    <div class="contact-lines">
      <p class="phone">0772 458 916</p>
      <p>INFO@BRACKENFOLDLAWN.CO.UK</p>
      <p>WWW.<span class="highlight">BRACKENFOLDLAWN</span>.CO.UK</p>
    </div>
  </section>

  <section class="card back" aria-label="Business card back">
    <div class="brand">
      <div class="brand-mark"></div>
      <p class="brand-name">THE BRACKENFOLD</p>
      <p class="brand-sub">LAWNCARE COMPANY LTD</p>
    </div>

    <ul class="social-list">
      <li class="social-item"><span class="social-badge"></span><span class="social-handle">TheBrackenfoldLawncareCompany</span></li>
      <li class="social-item"><span class="social-badge"></span><span class="social-handle">ThePlotTruck</span></li>
      <li class="social-item"><span class="social-badge"></span><span class="social-handle">thebrackenfoldlawncarecompany</span></li>
      <li class="social-item"><span class="social-badge"></span><span class="social-handle">thebrackenfoldlawncarecompany</span></li>
      <li class="social-item"><span class="social-badge"></span><span class="social-handle long">the-brackenfold-lawncare-company-manchester-4</span></li>
    </ul>
  </section>

</main>
</body>
</html>
```